U.S. based testing, inspection, and certification (TIC) company needs a new PowerPoint template.

We need a new PowerPoint template (deck, slide deck) for our U.S. based company with international capabilities for performing numerous testing, inspection, and certification (TIC) services. Our primary services include calibration, chemical analysis, consulting engineering, environmental simulation, forensic engineering, materials testing, mechanical testing, and nondestructive testing. Industries we serve are aerospace/aviation, automotive, chemical, commercial properties, construction, consumer products, defense, energy storage, healthcare, insurance/legal, life science, manufacturing, oil & gas, power generation, pulp & paper, and telecommunications. https://qirvotest.com/

Guideline hex colors: #29aae2, #0b1f3b, #fb6805 (use orange more subtly)

The final design should communicate:
1. Trust, Integrity, and Independence
2. Technical Expertise and Accuracy
3. Efficiency and Speed
4. Value-Added Partnership

Our current branding reflects a variety of styles, several of which have been included as attachments for reference in this project. While these examples showcase the direction we have taken in the past, we are not limited to them and remain open to exploring fresh, innovative design that is simple, clean, and with plenty of space to add content for each slide. We welcome creative concepts that build on or reimagine our existing identity to better align with our evolving vision.

```html
<!DOCTYPE html>
<html lang="en">
<head>
<meta charset="utf-8">
<title>Nanotechnology Innovation – Slide Deck Overview</title>
<link href="https://fonts.googleapis.com/css2?family=Inter:ital,wght@0,400;0,600;0,700;1,600&display=swap" rel="stylesheet">
<style>
  :root{
    --navy:#0b1f3b;
    --panel:#3a659e;
    --blue:#29aae2;
    --white:#ffffff;
    --body:#d7e2ef;
    --band:#1b4a72;
    --photo-a:#4c7fa8;
    --photo-b:#c9d6e2;
  }
  *{margin:0;padding:0;box-sizing:border-box}
  html,body{width:1200px;height:546px;overflow:hidden;background:#fff;font-family:"Inter",sans-serif}
  .canvas{position:relative;width:1200px;height:546px}
  .section-tag{position:absolute;left:15px;top:2px;width:23px;height:10px;background:var(--panel);border-radius:2px;color:#fff;font-size:4px;line-height:10px;text-align:center}
  .board{position:absolute;left:15px;top:15px;width:1169px;height:514px;background:var(--panel)}
  .slide{position:absolute;width:281px;height:157px;background:var(--navy);overflow:hidden;color:var(--white)}
  .abs{position:absolute}
  .title{font-weight:400;font-size:23px;line-height:21px;letter-spacing:-.4px;text-transform:uppercase}
  .blue{color:var(--blue)}
  .kicker{font-size:9px;line-height:10px;text-transform:uppercase;letter-spacing:-.1px}
  .body{font-size:3.6px;line-height:4.3px;color:var(--body)}
  .label{font-size:4.4px;font-weight:600;line-height:5px}
  .logo{font-size:4px;display:flex;align-items:center;gap:1.5px}
  .logo i{width:3px;height:3px;border-radius:50%;background:var(--blue);display:block}
  .vbar{position:absolute;width:1px;background:var(--blue)}
  .photo{position:absolute;background:linear-gradient(135deg,var(--photo-a),var(--photo-b))}
  .band{position:absolute;background:linear-gradient(180deg,var(--band),rgba(27,74,114,0))}
  .band-h{position:absolute;background:linear-gradient(90deg,var(--band),rgba(27,74,114,0))}
  .point{display:flex;align-items:center;gap:2px}
  .point svg{flex:none}
  .icon-ring{position:absolute;width:16px;height:16px;border:.6px solid var(--blue);border-radius:50%;display:flex;align-items:center;justify-content:center}
  .num{display:inline-flex;width:6px;height:6px;border:.4px solid #6d86a6;border-radius:50%;font-size:3.6px;align-items:center;justify-content:center;margin-right:3px}
</style>
</head>
<body>
<div class="canvas">
  <div class="section-tag">Section 1</div>
  <div class="board"></div>

  <!-- 1 Title -->
  <section class="slide" style="left:30px;top:30px;background:radial-gradient(ellipse at 50% 40%,#1c3f74,#0b1f3b 80%)">
    <div class="band" style="left:0;top:46px;width:14px;height:65px;background:linear-gradient(90deg,#1f4c7a,rgba(31,76,122,0))"></div>
    <div class="band" style="right:0;top:46px;width:14px;height:65px;background:linear-gradient(270deg,#1f4c7a,rgba(31,76,122,0))"></div>
    <div class="abs logo" style="left:130px;top:17px"><i></i>LOGO</div>
    <div class="vbar" style="left:22px;top:65px;height:28px"></div>
    <div class="vbar" style="left:259px;top:65px;height:28px"></div>
    <div class="abs title blue" style="left:0;width:281px;top:58px;font-size:21px;line-height:20px;text-align:center">Nanotechnology<br>Innovation</div>
    <div class="abs body" style="left:16px;top:131px;color:#fff">Transforming Industries at<br>the Smallest Scale</div>
    <div class="abs" style="left:0;width:281px;top:130px;text-align:center;font-size:3.8px;color:var(--blue)">Presented by<br><span style="color:#fff;font-size:5px;font-weight:600">Dana Whitfield</span></div>
    <div class="abs body" style="right:16px;top:136px;color:#fff">www.qirvotest.com</div>
  </section>

  <!-- 2 What is -->
  <section class="slide" style="left:316px;top:30px">
    <div class="abs logo" style="right:16px;top:16px"><i></i>LOGO</div>
    <div class="abs kicker" style="left:16px;top:18px;font-size:14px;line-height:14px">What is</div>
    <div class="abs title blue" style="left:16px;top:32px">Nanotechnology</div>
    <div class="band-h" style="left:0;top:84px;width:16px;height:58px"></div>
    <div class="photo" role="img" aria-label="Scientist in protective gear examining a sample in a lab" style="left:16px;top:84px;width:100px;height:58px"></div>
    <div class="vbar" style="left:141px;top:100px;height:23px"></div>
    <div class="abs body" style="left:157px;top:89px;width:68px">Nanotechnology involves working with materials at the scale of atoms and molecules, typically between 1 and 100 nanometers.<br><br>At this scale, materials exhibit unique properties that differ significantly from their larger forms, enabling breakthroughs in science and engineering.</div>
  </section>

  <!-- 3 Why matters -->
  <section class="slide" style="left:603px;top:30px">
    <div class="abs logo" style="right:16px;top:16px"><i></i>LOGO</div>
    <div class="abs title" style="left:16px;top:16px"><span class="blue">Why<br>Nanotechnology</span><br>Matters</div>
    <div class="vbar" style="left:260px;top:42px;height:12px"></div>
    <div class="band" style="right:0;top:90px;width:7px;height:50px"></div>
    <div class="abs label point" style="left:16px;top:112px"><svg width="8" height="3"><line x1="0" y1="1.5" x2="5" y2="1.5" stroke="#29aae2" stroke-width=".6"/><circle cx="6.4" cy="1.5" r="1.1" fill="none" stroke="#29aae2" stroke-width=".6"/></svg>Efficiency Improvement</div>
    <div class="abs label point" style="left:16px;top:124px"><svg width="8" height="3"><line x1="0" y1="1.5" x2="5" y2="1.5" stroke="#29aae2" stroke-width=".6"/><circle cx="6.4" cy="1.5" r="1.1" fill="none" stroke="#29aae2" stroke-width=".6"/></svg>Sustainability</div>
    <div class="abs label point" style="left:16px;top:136px"><svg width="8" height="3"><line x1="0" y1="1.5" x2="5" y2="1.5" stroke="#29aae2" stroke-width=".6"/><circle cx="6.4" cy="1.5" r="1.1" fill="none" stroke="#29aae2" stroke-width=".6"/></svg>Advanced Functionality</div>
    <div class="photo" role="img" aria-label="Two researchers working at a microscope" style="left:104px;top:98px;width:68px;height:44px"></div>
    <div class="abs body" style="left:186px;top:93px;width:76px">Nanotechnology plays an increasingly crucial role in addressing the complex challenges of the modern era by dramatically improving mechanical and operational efficiency.<br><br>It significantly reduces environmental waste through precision manufacturing and the more effective use of raw materials.</div>
  </section>

  <!-- 4 Applications -->
  <section class="slide" style="left:889px;top:30px">
    <div class="band" style="left:11px;top:80px;width:55px;height:78px;background:linear-gradient(0deg,#1b4a72,rgba(27,74,114,0))"></div>
    <div class="band" style="left:147px;top:80px;width:55px;height:78px;background:linear-gradient(0deg,#1b4a72,rgba(27,74,114,0))"></div>
    <div class="abs title" style="left:16px;top:16px;font-size:21px">Applications of</div>
    <div class="abs blue" style="left:16px;top:35px;font-size:15px;line-height:15px">NANOTECHNOLOGY</div>
    <div class="abs label" style="left:16px;top:74px">HEALTHCARE</div>
    <div class="abs label" style="left:84px;top:74px">ELECTRONICS</div>
    <div class="abs label" style="left:151px;top:74px">ENERGY</div>
    <div class="abs label" style="left:219px;top:74px">SCIENCE</div>
    <div class="photo" role="img" aria-label="Doctor attending a patient" style="left:16px;top:85px;width:46px;height:34px"></div>
    <div class="photo" role="img" aria-label="Close-up of a circuit board" style="left:84px;top:85px;width:46px;height:34px;background:linear-gradient(135deg,#5a4a3a,#a89884)"></div>
    <div class="photo" role="img" aria-label="Solar panel in a field" style="left:151px;top:85px;width:46px;height:34px;background:linear-gradient(180deg,#8ab4dc,#3c5e88)"></div>
    <div class="photo" role="img" aria-label="Gloved hand handling lab glassware" style="left:219px;top:85px;width:46px;height:34px"></div>
    <div class="abs body" style="left:16px;top:127px;width:46px">Enables advanced drug delivery and more accurate diagnostics for improved treatment outcomes.</div>
    <div class="abs body" style="left:84px;top:127px;width:46px">Supports smaller, faster, and more efficient devices with better performance.</div>
    <div class="abs body" style="left:151px;top:127px;width:46px">Improves energy storage and increases efficiency in various energy systems.</div>
    <div class="abs body" style="left:219px;top:127px;width:46px">Enhances material strength and durability while keeping them lightweight.</div>
  </section>

  <!-- 5 Market -->
  <section class="slide" style="left:30px;top:194px">
    <div class="band-h" style="left:0;top:16px;width:16px;height:57px"></div>
    <div class="photo" role="img" aria-label="Close-up of a green circuit board with a chip" style="left:16px;top:16px;width:100px;height:57px;background:linear-gradient(135deg,#2a3a32,#5e8a7a)"></div>
    <div class="vbar" style="left:141px;top:33px;height:23px"></div>
    <div class="abs body" style="left:197px;top:34px;width:70px">Nanotechnology presents exceptionally significant growth opportunities in the current global market, primarily driven by a rapidly increasing demand for advanced materials and specialized applications across numerous sectors.<br><br>This surge in interest is fueled by the unique ability of nanoscale engineering to enhance product performance, which in turn creates a competitive advantage for early adopters in high-tech fields.</div>
    <div class="abs title blue" style="left:16px;top:89px">Market<br>Opportunity</div>
    <div class="abs" style="left:16px;top:134px;font-size:7px;text-transform:uppercase">Growing demand for nanotechnology</div>
  </section>

  <!-- 6 Stands out -->
  <section class="slide" style="left:316px;top:194px">
    <div class="abs kicker" style="left:16px;top:16px">Why nanotechnology</div>
    <div class="abs title blue" style="left:16px;top:28px">Stands out</div>
    <div class="photo" role="img" aria-label="Gloved hand with lab equipment" style="left:205px;top:34px;width:60px;height:45px"></div>
    <div class="band-h" style="left:0;top:83px;width:22px;height:70px"></div>
    <div class="vbar" style="left:30px;top:94px;height:36px"></div>
    <div class="abs" style="left:58px;top:84px;width:110px;font-size:3.8px;font-weight:600;font-style:italic;line-height:4.5px">Nanotechnology provides unique advantages that differentiate it from traditional solutions.</div>
    <div class="abs" style="left:58px;top:103px;width:100px"><div class="label"><span class="num">1.</span>High Precision</div><div class="body" style="padding-left:9px">Nanotechnology enables highly accurate results by controlling materials at the molecular level.</div></div>
    <div class="abs" style="left:165px;top:103px;width:100px"><div class="label"><span class="num">3.</span>Scalability</div><div class="body" style="padding-left:9px">The technology can be applied across multiple industries and adapted to different use cases.</div></div>
    <div class="abs" style="left:58px;top:127px;width:100px"><div class="label"><span class="num">2.</span>Enhanced Performance</div><div class="body" style="padding-left:9px">It improves efficiency and overall functionality across various applications.</div></div>
    <div class="abs" style="left:165px;top:127px;width:100px"><div class="label"><span class="num">4.</span>Future-Ready</div><div class="body" style="padding-left:9px">It offers long-term value by supporting continuous innovation and technological advancement.</div></div>
  </section>

  <!-- 7 Challenges -->
  <section class="slide" style="left:603px;top:194px">
    <div class="abs kicker" style="left:16px;top:16px">Navigating the challenges of</div>
    <div class="abs title blue" style="left:16px;top:28px">Nanotechnology</div>
    <div class="band-h" style="left:0;top:73px;width:8px;height:68px"></div>
    <div class="abs body" style="left:16px;top:87px;width:70px">While nanotechnology offers groundbreaking potential across multiple industries, its development and adoption come with several challenges that must be carefully addressed. From high research costs to complex technical requirements, these barriers can slow down innovation and limit accessibility.<br><br>In addition, strict regulatory frameworks and limited public understanding can affect how quickly nanotechnology solutions are accepted and implemented.</div>
    <div class="photo" role="img" aria-label="Researcher in a lab coat holding documents in a corridor" style="left:100px;top:73px;width:71px;height:68px;background:linear-gradient(180deg,#cfd6dc,#8c99a4)"></div>
    <div class="vbar" style="left:188px;top:89px;height:24px"></div>
    <div class="icon-ring" style="left:208px;top:71px"><svg width="8" height="8" viewBox="0 0 8 8" fill="none" stroke="#fff" stroke-width=".5"><path d="M1 4.5 4.5 1H7v2.5L3.5 7z"/><circle cx="5.5" cy="2.5" r=".5"/></svg></div>
    <div class="icon-ring" style="left:243px;top:71px"><svg width="8" height="8" viewBox="0 0 8 8" fill="none" stroke="#fff" stroke-width=".5"><rect x="1.5" y="1" width="5" height="6"/><path d="M2.5 3h3M2.5 4.5h3M2.5 6h2"/></svg></div>
    <div class="icon-ring" style="left:208px;top:108px"><svg width="8" height="8" viewBox="0 0 8 8" fill="none" stroke="#fff" stroke-width=".5"><circle cx="3.5" cy="3.5" r="2.3"/><path d="M5.2 5.2 7 7"/></svg></div>
    <div class="icon-ring" style="left:243px;top:108px"><svg width="8" height="8" viewBox="0 0 8 8" fill="none" stroke="#fff" stroke-width=".5"><circle cx="2.8" cy="2.5" r="1"/><circle cx="5.3" cy="2.5" r="1"/><path d="M1 6.5c0-1.5 3.6-1.5 3.6 0M3.5 6.5c0-1.5 3.6-1.5 3.6 0"/></svg></div>
    <div class="abs label" style="left:196px;top:93px;width:40px;text-align:center">High Costs</div>
    <div class="abs label" style="left:231px;top:93px;width:40px;text-align:center">Regulation</div>
    <div class="abs label" style="left:196px;top:131px;width:40px;text-align:center">Technical<br>Complexety</div>
    <div class="abs label" style="left:231px;top:131px;width:40px;text-align:center">Public<br>Awareness</div>
  </section>

  <!-- 8 What's next -->
  <section class="slide" style="left:889px;top:194px">
    <div class="band" style="left:129px;top:0;width:56px;height:16px;background:linear-gradient(0deg,#1b4a72,rgba(27,74,114,.2))"></div>
    <div class="photo" role="img" aria-label="Scientist working with samples in petri dishes" style="left:129px;top:16px;width:56px;height:34px;background:linear-gradient(135deg,#e8e2dc,#c6a8b0)"></div>
    <div class="abs kicker" style="left:16px;top:52px">What's next in</div>
    <div class="abs title blue" style="left:16px;top:63px">Nanotechnology</div>
    <div class="vbar" style="left:69px;top:101px;height:14px"></div>
    <div class="abs body" style="left:80px;top:97px;width:66px">Nanotechnology continues to evolve rapidly, driven by emerging trends that are reshaping how industries innovate and solve complex challenges.</div>
    <div class="abs body" style="left:154px;top:97px;width:96px">These future trends highlight how the field is moving toward smarter systems, groundbreaking materials, and transformative solutions that will define the next generation of technological development.</div>
    <div class="abs label point" style="left:16px;top:137px"><svg width="8" height="3"><line x1="0" y1="1.5" x2="5" y2="1.5" stroke="#29aae2" stroke-width=".6"/><circle cx="6.4" cy="1.5" r="1.1" fill="none" stroke="#29aae2" stroke-width=".6"/></svg>Medical Breakthrough</div>
    <div class="abs label point" style="left:106px;top:137px"><svg width="8" height="3"><line x1="0" y1="1.5" x2="5" y2="1.5" stroke="#29aae2" stroke-width=".6"/><circle cx="6.4" cy="1.5" r="1.1" fill="none" stroke="#29aae2" stroke-width=".6"/></svg>Sustainable Technology</div>
    <div class="abs label point" style="left:203px;top:137px"><svg width="8" height="3"><line x1="0" y1="1.5" x2="5" y2="1.5" stroke="#29aae2" stroke-width=".6"/><circle cx="6.4" cy="1.5" r="1.1" fill="none" stroke="#29aae2" stroke-width=".6"/></svg>AI Integration</div>
  </section>

  <!-- 9 Project potential -->
  <section class="slide" style="left:30px;top:357px">
    <div class="abs title blue" style="left:16px;top:20px">Project<br>Potential</div>
    <div class="band-h" style="left:0;top:83px;width:22px;height:59px"></div>
    <div class="vbar" style="left:30px;top:94px;height:37px"></div>
    <div class="photo" role="img" aria-label="Technician reviewing a scan on a monitor" style="left:52px;top:83px;width:100px;height:59px;background:linear-gradient(135deg,#9aa6ae,#e2e6e8)"></div>
    <div class="abs" style="left:173px;top:55px;width:90px"><div class="label point"><svg width="8" height="3"><line x1="0" y1="1.5" x2="5" y2="1.5" stroke="#29aae2" stroke-width=".6"/><circle cx="6.4" cy="1.5" r="1.1" fill="none" stroke="#29aae2" stroke-width=".6"/></svg>Product Development</div><div class="body" style="padding-left:12px;margin-top:2px">Enables the creation of innovative solutions with enhanced performance and new capabilities across industries.</div></div>
    <div class="abs" style="left:173px;top:88px;width:90px"><div class="label point"><svg width="8" height="3"><line x1="0" y1="1.5" x2="5" y2="1.5" stroke="#29aae2" stroke-width=".6"/><circle cx="6.4" cy="1.5" r="1.1" fill="none" stroke="#29aae2" stroke-width=".6"/></svg>Process Improvement</div><div class="body" style="padding-left:12px;margin-top:2px">Improves efficiency by optimizing production methods and reducing time, cost, and resource usage.</div></div>
    <div class="abs" style="left:173px;top:120px;width:90px"><div class="label point"><svg width="8" height="3"><line x1="0" y1="1.5" x2="5" y2="1.5" stroke="#29aae2" stroke-width=".6"/><circle cx="6.4" cy="1.5" r="1.1" fill="none" stroke="#29aae2" stroke-width=".6"/></svg>Market Expansion</div><div class="body" style="padding-left:12px;margin-top:2px">Opens new opportunities by entering emerging markets and addressing diverse industry needs.</div></div>
  </section>

  <!-- 10 Closing -->
  <section class="slide" style="left:316px;top:357px">
    <div class="abs title" style="left:16px;top:15px;line-height:22px">Invest in the<br><span class="blue">Future of</span><br>Innovation</div>
    <div class="vbar" style="left:197px;top:46px;height:21px"></div>
    <div class="photo" role="img" aria-label="Gloved hand with lab equipment" style="left:205px;top:34px;width:60px;height:45px"></div>
    <div class="band-h" style="left:265px;top:34px;width:16px;height:45px;background:linear-gradient(270deg,#1b4a72,rgba(27,74,114,.2))"></div>
    <div class="abs body" style="left:16px;top:128px;width:85px;color:#fff">Nanotechnology represents a powerful opportunity to drive innovation, improve efficiency, and create sustainable solutions.</div>
    <div class="abs label point blue" style="left:193px;top:112px"><svg width="10" height="3"><line x1="0" y1="1.5" x2="7" y2="1.5" stroke="#29aae2" stroke-width=".6"/><circle cx="8.4" cy="1.5" r="1.1" fill="none" stroke="#29aae2" stroke-width=".6"/></svg>Get in touch with us!</div>
    <div class="abs" style="left:206px;top:124px;font-size:4.4px;line-height:6.5px">@brightlabnote<br>hello@brightlabnote.com<br>www.brightlabnote.com</div>
  </section>
</div>
</body>
</html>
```